Velora Beauty Clinic

I need a web design for a Cosmetic Surgery Clinic. The current site is velora-beauty-clinic.example. The design should be:
- Flat Design with big banner
- Warm colors
- Responsive Layout
- SEO friendly

Cosmetic

```html
<!DOCTYPE html>
<html lang="en">
<head>
<meta charset="utf-8">
<title>Velora Beauty Clinic</title>
<link rel="stylesheet" href="https://fonts.googleapis.com/css2?family=Roboto+Condensed:wght@300;400&family=Source+Sans+3:wght@400;600;700&display=swap">
<style>
  :root {
    --pink: #e84a96;
    --pink-deep: #bb2068;
    --magenta: #a8155d;
    --ink: #1c1c1c;
    --charcoal: #333333;
    --white: #ffffff;
    --text: #333333;
    --photo-a: #dcdfe4;
    --photo-b: #c9c7d8;
    --photo-c: #c2c2c4;
  }
  * { box-sizing: border-box; margin: 0; padding: 0; }
  html, body { width: 1200px; height: 1015px; overflow: hidden; background: var(--white); }
  body { font-family: "Source Sans 3", sans-serif; color: var(--text); }

  .condensed { font-family: "Roboto Condensed", sans-serif; }

  .blog { height: 493px; background: var(--pink); padding-top: 56px; text-align: center; }
  .blog-title { font-family: "Roboto Condensed", sans-serif; font-weight: 300; font-size: 36px; color: var(--white); line-height: 44px; height: 62px; }
  .cards { display: flex; gap: 28px; padding: 0 38px; }
  .card { width: 356px; }
  .card-photo { height: 188px; }
  .card-photo.one { background: linear-gradient(135deg, #eef0f2, var(--photo-a)); }
  .card-photo.two { background: linear-gradient(135deg, #b9b4e6, #f1ece8 55%, #e9c9a9); }
  .card-photo.three { background: linear-gradient(180deg, var(--photo-c), #d8c0ae); }
  .card-caption { height: 46px; line-height: 46px; background: var(--pink-deep); color: var(--white); font-size: 15px; }
  .outline-btn { display: inline-block; border: 1px solid var(--white); color: var(--white); font-family: "Roboto Condensed", sans-serif; font-size: 23px; width: 320px; height: 42px; line-height: 40px; text-align: center; }
  .blog .outline-btn { margin-top: 29px; }

  .consult { height: 231px; background: var(--ink); text-align: center; padding-top: 60px; }
  .consult-title { font-family: "Roboto Condensed", sans-serif; font-weight: 300; font-size: 36px; color: var(--pink); line-height: 44px; }
  .consult-row { margin-top: 19px; display: flex; justify-content: center; align-items: center; gap: 14px; color: var(--white); font-size: 23px; }
  .consult-row strong { font-weight: 700; }
  .consult-row .or { margin: 0 0 0 2px; }

  .signup { height: 70px; background: var(--charcoal); display: flex; align-items: center; padding: 0 38px; }
  .social { display: flex; gap: 3.5px; }
  .social span { width: 34px; height: 34px; background: var(--pink-deep); }
  .signup-label { margin-left: auto; font-family: "Roboto Condensed", sans-serif; font-size: 18px; color: var(--white); margin-right: 10px; }
  .email { width: 347px; height: 42px; background: var(--white); font-family: Arial, sans-serif; font-size: 13px; color: #666; line-height: 42px; padding-left: 9px; }
  .submit { margin-left: 9px; width: 133px; height: 42px; border: 1px solid var(--white); color: var(--white); font-family: "Roboto Condensed", sans-serif; font-size: 23px; line-height: 40px; text-align: center; }

  .legal { height: 65px; background: var(--magenta); color: var(--white); font-size: 13.5px; text-align: center; line-height: 65px; }
  .legal strong { font-weight: 700; }

  .about { padding: 27px 38px 0; }
  .about h2 { font-size: 13px; font-weight: 700; text-transform: uppercase; line-height: 20px; }
  .about p { font-size: 13.5px; line-height: 22.5px; text-align: justify; }
</style>
</head>
<body>
  <section class="blog">
    <h1 class="blog-title">COSMETIC SURGERY BLOG</h1>
    <div class="cards">
      <article class="card">
        <div class="card-photo one" role="img" aria-label="Photo of a woman with facial contour lines marked on her skin"></div>
        <div class="card-caption">A Guide To Cosmetic Surgery in Cyprus</div>
      </article>
      <article class="card">
        <div class="card-photo two" role="img" aria-label="Photo of a surgeon examining a patient before a procedure"></div>
        <div class="card-caption">Cosmetic Surgery Abroad</div>
      </article>
      <article class="card">
        <div class="card-photo three" role="img" aria-label="Photo of a torso with dotted surgical guide lines"></div>
        <div class="card-caption">Cost of Cosmetic Surgery Procedures</div>
      </article>
    </div>
    <a class="outline-btn">READ ALL NEWS</a>
  </section>

  <section class="consult">
    <h2 class="consult-title">READY FOR A CONSULTATION?</h2>
    <div class="consult-row">
      <span>Call Us: <strong>0700 555 0148</strong></span>
      <span class="or">or</span>
      <a class="outline-btn">SCHEDULE A CONSULTATION</a>
    </div>
  </section>

  <section class="signup">
    <div class="social" aria-label="Social links">
      <span></span><span></span><span></span><span></span><span></span>
    </div>
    <div class="signup-label">SIGN UP FOR MONTHLY COUPONS</div>
    <div class="email">Enter Email Address</div>
    <div class="submit">SUBMIT</div>
  </section>

  <footer class="legal">
    © 1994–2015 &nbsp;<strong>Velora-Beauty-Clinic</strong> | All rights reserved. | Privacy Policy | Terms &amp; Conditions | Sitemap
  </footer>

  <section class="about">
    <h2>Cosmetic Surgery Holiday Packages in Cyprus</h2>
    <p>If you are considering medical tourism, Velora Beauty Clinic can offer you tailor made affordable cosmetic surgery holiday packages in Cyprus including accommodation and travel arrangements that suit your specific needs. We offer you top quality cosmetic surgery procedures abroad at affordable cosmetic surgery prices with dedicated aftercare. We can offer a broad range of procedures including breast surgery abroad, facial cosmetic surgery, liposuction or tummy tuck surgery. Make the right decision for your cosmetic surgery abroad with Velora Beauty Clinic and we will organise your whole stay in beautiful Cyprus, in a discreet, English-speaking, friendly and safe environment, so you can concentrate on your beauty and relax and recuperate in a stress free environment .</p>
  </section>
</body>
</html>
```